cover for CD- Single.

This design is for a CD cover. The design is at your disposal, using all of your creative talents.
Things to improve the photo: Cleaning the face, removing blemishes.
Design in black and white would be an option (Color would be another option). I reiterate it is up to your taste and criteria, any reform and art on the cover of Cd.
Name of the single: El Camino del Silencio
Artist Name: Marisol Duarte

Target Market(s)

Single Music

Industry/Entity Type

Music

Colors

Designer to choose colors to be used in the design.

Requirements
Must have
• style, elegance, professionalism, spontaneity
Nice to have
• I want it to be as professional as possible.
Should not have
• Spelling errors.

```html
<!DOCTYPE html>
<html lang="es">
<head>
<meta charset="utf-8">
<title>El Camino del Silencio — Marisol Duarte</title>
<link href="https://fonts.googleapis.com/css2?family=Bebas+Neue&family=Marcellus&display=swap" rel="stylesheet">
<style>
  :root {
    --backdrop: #282828;
    --cover-black: #0b0b0b;
    --photo-light: #d9d9d9;
    --photo-mid: #7a7a7a;
    --title-white: #f0f0f0;
    --subtitle-grey: #c4c4c4;
    --artist-grey: #b8b8b8;
  }
  * { margin: 0; padding: 0; box-sizing: border-box; }
  html, body {
    width: 1200px;
    height: 1002px;
    overflow: hidden;
    background: var(--backdrop);
  }
  .cd-cover {
    position: absolute;
    left: 357px;
    top: 255px;
    width: 486px;
    height: 486px;
    background: var(--cover-black);
    overflow: hidden;
  }
  .portrait {
    position: absolute;
    inset: 0;
    background:
      radial-gradient(ellipse 48% 44% at 50% 36%, var(--photo-light) 0%, #b5b5b5 45%, rgba(90,90,90,0.6) 75%, rgba(11,11,11,0) 100%),
      radial-gradient(ellipse 22% 40% at 88% 62%, rgba(200,200,200,0.7) 0%, rgba(11,11,11,0) 100%),
      linear-gradient(180deg, #f2f2f2 0%, rgba(11,11,11,0) 22%),
      var(--cover-black);
  }
  .portrait::after {
    content: "";
    position: absolute;
    inset: 0;
    background: linear-gradient(180deg, rgba(11,11,11,0) 55%, rgba(11,11,11,0.85) 80%, var(--cover-black) 100%),
                linear-gradient(90deg, var(--cover-black) 0%, rgba(11,11,11,0) 20%);
  }
  .cover-titles {
    position: absolute;
    left: 0;
    right: 0;
    top: 312px;
    text-align: center;
  }
  .single-subtitle {
    font-family: "Marcellus", serif;
    font-size: 21px;
    color: var(--subtitle-grey);
    letter-spacing: 0.5px;
    line-height: 1;
  }
  .single-title {
    font-family: "Bebas Neue", sans-serif;
    font-size: 132px;
    color: var(--title-white);
    line-height: 0.9;
    letter-spacing: 2px;
    margin-top: 2px;
  }
  .artist-name {
    font-family: "Marcellus", serif;
    font-size: 13px;
    color: var(--artist-grey);
    letter-spacing: 3px;
    line-height: 1;
    margin-top: 2px;
  }
</style>
</head>
<body>
  <main class="cd-cover">
    <div class="portrait" role="img" aria-label="Black and white close-up portrait of the singer with eyes closed, hand resting by her ear"></div>
    <div class="cover-titles">
      <p class="single-subtitle">El Camino del</p>
      <h1 class="single-title">SILENCIO</h1>
      <p class="artist-name">MARISOL DUARTE</p>
    </div>
  </main>
</body>
</html>
```